Nursing Concepts Diagram

We are looking to make a diagram to represent the Conceptual Framework of our nursing program (college). The frame work is based on three parts:

I. Nursing Process

II. Core Concepts
a. Clinical Competence
b. Critical Thinking
c. Moral/Ethical Principles
d. Growth Mindset
e. Caring/Compassion
f. Cultural Competence
g. Effective Communication
h. Life-long Learning

III. Brennick's Hierarchy of Needs

I have attached two sketches to give you a sense of how I think this could work.

Please also consider the following:

-Brennick's Hierarchy of Needs is always represented in the shape of a pyramid so I think the other two components (Nursing Process and Core Concepts) should complement that.

Target Market(s)

Healthcare Professionals, Nursing Educators

Font styles to use
Sans Serif

Colors

Designer to choose colors to be used in the design.

Requirements
Must have
• We would like the diagram to include a legend somewhere on the paper that outlines the parts of each component like demonstrated in the attached table
• All the small parts of the Nursing Process and Brennick's Hierarchy of Needs don't need to be listed out in the diagram because it may look too wordy, but the eight parts that make up the core concepts should all be listed
• The Nursing Process and Brennick's Hierachy of needs should both border each of the 8 core concepts so that it can show a relation.

```html
<!DOCTYPE html>
<html lang="en">
<head>
<meta charset="utf-8">
<title>Nursing Conceptual Framework</title>
<link rel="stylesheet" href="https://fonts.googleapis.com/css2?family=Poppins:wght@400;500;600&family=Oswald:wght@500&display=swap">
<style>
  :root {
    --bg: #ffffff;
    --heading: #1b6883;
    --legend-text: #333333;
    --outer: #00adee;
    --life: #ff0000;
    --caring: #c3a700;
    --growth: #ff6f00;
    --cultural: #22bf00;
    --clinical: #5a4a12;
    --critical: #e04848;
    --communication: #2f6558;
    --moral: #0a6cff;
    --core-light: #1ccda6;
    --core-dark: #0d7257;
    --title: #f4e7f8;
    --white: #ffffff;
  }
  html, body { margin: 0; padding: 0; overflow: hidden; background: var(--bg); }
  .canvas { position: relative; width: 1200px; height: 927px; overflow: hidden; background: var(--bg); }
  .legend { position: absolute; left: 27px; top: 0; font-family: "Poppins", sans-serif; }
  .legend-group { position: absolute; left: 0; width: 340px; }
  .legend-group h2 { margin: 0 0 10px; font-size: 20px; font-weight: 600; color: var(--heading); letter-spacing: .2px; }
  .legend-group ul { list-style: none; margin: 0; padding: 0; }
  .legend-group li { position: relative; padding-left: 18px; height: 27.3px; font-size: 15px; color: var(--legend-text); letter-spacing: .3px; }
  .legend-group li::before {
    content: "➲"; position: absolute; left: 0; top: 3px; width: 10px; height: 10px;
    border: 1px solid var(--legend-text); border-radius: 50%; font-size: 7px; line-height: 10px; text-align: center;
  }
  .group-process { top: 23px; }
  .group-core { top: 218px; }
  .group-needs { top: 510px; }
  .diagram { position: absolute; left: 0; top: 0; }
  .ring-label { font-family: "Poppins", sans-serif; font-weight: 500; font-size: 70px; fill: var(--white); letter-spacing: 9px; }
  .band-label { font-family: "Poppins", sans-serif; font-weight: 500; font-size: 15px; fill: var(--white); letter-spacing: 1.2px; }
  .core-title { font-family: "Oswald", sans-serif; font-weight: 500; fill: var(--title); letter-spacing: 4px; }
</style>
</head>
<body>
<div class="canvas">
  <div class="legend">
    <section class="legend-group group-process">
      <h2>Nursing Process</h2>
      <ul><li>Assessment</li><li>Nursing Diagnosis</li><li>Planning</li><li>Intervention</li><li>Evaluation</li></ul>
    </section>
    <section class="legend-group group-core">
      <h2>Core Concepts</h2>
      <ul><li>Clinical Competence</li><li>Critical Thinking</li><li>Moral/Ethical Principles</li><li>Growth Mindset</li><li>Caring/Compassion</li><li>Cultural Competence</li><li>Effective Communication</li><li>Life-long Learning</li></ul>
    </section>
    <section class="legend-group group-needs">
      <h2>Brennick’s Hierarchy of Needs</h2>
      <ul><li>Self-actualization</li><li>Esteem</li><li>Love and Belonging</li><li>Safety Needs</li><li>Physiological Needs</li></ul>
    </section>
  </div>

  <svg class="diagram" width="1200" height="927" viewBox="0 0 1200 927">
    <defs>
      <linearGradient id="core-fill" x1="0" y1="0" x2="1" y2="0">
        <stop offset="0.25" stop-color="var(--core-light)"/>
        <stop offset="1" stop-color="var(--core-dark)"/>
      </linearGradient>
    </defs>
    <polygon class="process-ring" points="723,42 1139,762 309,762" fill="var(--outer)"/>

    <polygon points="723,196 723,313 657,425 623,365" fill="var(--life)"/>
    <polygon points="623,365 657,425 580,553 521,538" fill="var(--caring)"/>
    <polygon points="521,538 580,553 518,658 415,718" fill="var(--growth)"/>
    <polygon points="415,718 518,658 723,658 723,718" fill="var(--communication)"/>
    <polygon points="723,658 930,658 1032,718 723,718" fill="var(--moral)"/>
    <polygon points="723,196 847,405 798,438 723,313" fill="var(--cultural)"/>
    <polygon points="847,405 941,565 890,591 798,438" fill="var(--clinical)"/>
    <polygon points="941,565 1032,718 930,658 890,591" fill="var(--critical)"/>

    <polygon class="needs-core" points="723,313 930,658 518,658" fill="url(#core-fill)"/>

    <text class="ring-label" text-anchor="middle" transform="translate(560,436) rotate(-59.5)">NURSING</text>
    <text class="ring-label" text-anchor="middle" transform="translate(893,430) rotate(59.5)">PROCESS</text>

    <g class="band-label" text-anchor="middle">
      <text transform="translate(672,312) rotate(-59.5)"><tspan x="0" y="-3">LIFE-LONG</tspan><tspan x="0" y="15">LEARNING</tspan></text>
      <text transform="translate(592,455) rotate(-59.5)"><tspan x="0" y="-3">CARING/</tspan><tspan x="0" y="15">COMPASSION</tspan></text>
      <text transform="translate(512,608) rotate(-59.5)"><tspan x="0" y="-3">GROWTH</tspan><tspan x="0" y="15">MINDSET</tspan></text>
      <text transform="translate(770,352) rotate(59.5)"><tspan x="0" y="-3">CULTURAL</tspan><tspan x="0" y="15">COMPETENCE</tspan></text>
      <text transform="translate(862,506) rotate(59.5)"><tspan x="0" y="-3">CLINICAL</tspan><tspan x="0" y="15">COMPETENCE</tspan></text>
      <text transform="translate(937,622) rotate(59.5)"><tspan x="0" y="-3">CRITICAL</tspan><tspan x="0" y="15">THINKING</tspan></text>
      <text x="608" y="685">EFFECTIVE</text><text x="608" y="706">COMMUNICATION</text>
      <text x="838" y="682">MORAL/</text><text x="838" y="703">ETHICAL PRINCIPLES</text>
    </g>

    <g class="core-title" text-anchor="middle">
      <text x="722" y="536" font-size="37">BRENNICK’S</text>
      <text x="722" y="583" font-size="44">HIERARCHY</text>
      <text x="722" y="628" font-size="37">OF NEEDS</text>
    </g>
  </svg>
</div>
</body>
</html>
```